Catering Company Needs a Web Page Design

I already have my logo, and so I'm moving onto the next phase.. the web page design. Platrix is a gourmet catering company based in orlando, fl, set to launch in 2015. I will have a store location to host cooking classes as well.... and will be uploading cooking demo videos to my website weekly. Id like a blog section, and about, a video section, contact form, Services, Menu Samples..... My logo and concept is modern, innovative, and fun! I am targeting middle class to upper middle class women, but i want the site to be super unique.

Industry/Entity Type

Catering

Requirements
Must have
• The front/main page must have the logo... and the lingo ledger's definition of "platrix". I like movement... maybe the top banner can move somehow.. Im not a web designer, so i wont really know until I start seeing some examples. For now I dont have photos of my own cooking, so if you could use stock photos of catering dishes.. I uploaded a transparent logo also, maybe that could be the top banner placed over a scene of expertly plated hordourves...

```html
<!DOCTYPE html>
<html lang="en">
<head>
<meta charset="utf-8">
<title>Platrix — Gourmet Catering &amp; Cooking Classes</title>
<link rel="stylesheet" href="https://fonts.googleapis.com/css2?family=Arimo:wght@400;700&display=swap">
<style>
:root{
  --page:#e9e6e1;
  --sidebar:rgba(236,240,243,.86);
  --ink:#3a3a3a;
  --ink-soft:#5a5a5a;
  --brand:#4a3b2b;
  --amber:#c48a45;
  --amber-deep:#a66f31;
  --amber-light:#d9a462;
  --teal-dark:#3d4f55;
  --teal-mid:#56686c;
  --slate:#2f3336;
  --slate-deep:#1f2224;
  --field:#c9c9c9;
  --field-text:#3c3c3c;
  --white:#ffffff;
  --button:#587785;
}
*{box-sizing:border-box;margin:0;padding:0}
html,body{width:1200px;height:2512px;overflow:hidden}
body{background:var(--page);font-family:"Arimo",Arial,sans-serif;color:var(--ink);position:relative}
.photo{position:absolute}
.abs{position:absolute}

/* header */
.hero{left:0;top:0;width:1200px;height:575px;background:radial-gradient(ellipse at 62% 45%,#b06b57 0%,#8a5a3e 22%,#5c4a3a 42%,#8d9aa3 70%,#c9d3d8 100%)}
.sidebar{left:100px;top:0;width:232px;height:575px;background:var(--sidebar)}
.logo{left:112px;top:74px;display:flex;align-items:center;gap:6px}
.logo-name{font-weight:700;font-size:58px;color:var(--brand);letter-spacing:-1px;line-height:1}
.logo-tag{left:112px;top:136px;font-size:10px;color:var(--amber-deep);width:210px}
.nav{left:100px;top:202px;width:232px;list-style:none;text-align:center}
.nav li{font-size:19px;color:#222;height:77px;line-height:24px}

/* strip */
.strip{left:0;top:575px;width:1200px;height:128px;background:linear-gradient(var(--amber-light),var(--amber))}
.strip-arrow{top:620px}
.thumb{top:592px;width:158px;height:98px;border:4px solid #f3f0ea;background:linear-gradient(135deg,#e6e4e0,#9a8c7c 60%,#5d4c3c)}

/* welcome */
.welcome{left:100px;top:762px;width:995px;font-size:18.5px;line-height:22px;color:var(--ink-soft);text-align:center}
.feature{top:905px;height:215px}
.feature-label{top:1120px;height:37px;background:var(--amber);color:var(--white);font-size:18px;text-align:center;line-height:37px;letter-spacing:.5px}

/* videos */
.videos{left:0;top:1235px;width:1200px;height:655px;background:radial-gradient(ellipse at 40% 50%,var(--teal-mid),var(--teal-dark))}
.videos-title{left:100px;top:1350px;width:230px;text-align:center;color:var(--white);font-size:19px;font-weight:400}
.videos-copy{left:100px;top:1400px;width:230px;text-align:center;color:#eef1f2;font-size:18px;line-height:20px}
.videos-copy p+p{margin-top:22px}
.video-card{background:var(--white);padding:6px 6px 0}
.video-thumb{position:relative;width:100%;display:flex;align-items:center;justify-content:center}
.video-cap{font-size:11px;line-height:12px;color:#555;text-align:center;padding:5px 2px}
.more{left:670px;top:1780px;color:var(--white);font-size:17px;display:flex;align-items:center;gap:6px}

/* order */
.order{left:0;top:1890px;width:1200px;height:480px;background:radial-gradient(ellipse at 45% 45%,#6a6e70,var(--slate) 60%,var(--slate-deep))}
.order-title{left:172px;top:1962px;color:var(--white);font-size:27px;font-weight:400}
.order-copy{left:162px;top:2012px;width:250px;color:#e6e6e6;font-size:12.5px;line-height:14px;text-align:center}
.order-copy p+p{margin-top:12px}
.subscribe{left:246px;top:2130px;width:130px;height:104px;background:var(--button);border:2px solid #7f9aa6;color:var(--white);font-size:12px;text-align:center;display:flex;flex-direction:column;align-items:center;justify-content:center;gap:14px}
.field{left:488px;width:410px;height:26px;background:var(--field);color:var(--field-text);font-size:12px;line-height:14px;padding:1px 6px;position:absolute}
.field-line{position:absolute;left:0;right:0;bottom:0;height:12px;background:#dcdcdc}

/* footer */
.footer{left:0;top:2370px;width:1200px;height:142px;background:var(--slate-deep)}
.foot-rule{left:100px;top:2375px;width:1000px;height:1px;background:#5a5d60}
.foot-div{top:2385px;width:1px;height:112px;background:#6a6d70}
.foot-nav{left:215px;top:2396px;list-style:none;color:#e4e4e4;font-size:12.5px;line-height:15px}
.foot-center{left:495px;top:2392px;width:240px;text-align:center;color:#e4e4e4;font-size:12px;line-height:15px}
.foot-mail{left:860px;top:2404px;width:180px;text-align:center;color:#e4e4e4;font-size:12px}
</style>
</head>
<body>

<header>
  <div class="photo hero" role="img" aria-label="Plated roasted lamb slices over lentils and root vegetables"></div>
  <div class="abs sidebar"></div>
  <div class="abs logo"><span class="logo-name">platrix</span></div>
  <div class="abs logo-tag">Gourmet Catering &amp; Cooking Classes</div>
  <ul class="abs nav">
    <li>HOME</li><li>ABOUT</li><li>MENU</li><li>BLOG</li><li>LOCATION</li>
  </ul>
</header>

<section class="gallery-strip">
  <div class="abs strip"></div>
  <svg class="abs strip-arrow" style="left:92px" width="22" height="36" viewBox="0 0 22 36"><path d="M18 2 4 18l14 16" fill="none" stroke="#3a3a3a" stroke-width="6"/></svg>
  <svg class="abs strip-arrow" style="left:1068px" width="22" height="36" viewBox="0 0 22 36"><path d="M4 2l14 16L4 34" fill="none" stroke="#3a3a3a" stroke-width="6"/></svg>
  <div class="photo thumb" style="left:140px" role="img" aria-label="Canapés on a slate board"></div>
  <div class="photo thumb" style="left:322px" role="img" aria-label="Dessert plate with berries"></div>
  <div class="photo thumb" style="left:498px" role="img" aria-label="Main course on a white plate"></div>
  <div class="photo thumb" style="left:682px" role="img" aria-label="Plated meat with garnish"></div>
  <div class="photo thumb" style="left:872px" role="img" aria-label="Soup in a white bowl"></div>
</section>

<section class="intro">
  <p class="abs welcome">Welcome to the Platrix Gourmet Catering and Cooking Classes web site. Our web site will provide you with all the information you require to plan your unique menu for any special event. Whether for an Edmonton Wedding, Private Dinner Party, a Corporate Barbecue or anything involving food, please allow us to cater to your every need. Our Professional Catering Staff will pamper you at your event, using exquisite menus created by our exceptional Culinary Team, using only the Freshest Ingredients</p>

  <div class="photo feature" style="left:100px;width:310px;background:linear-gradient(135deg,#cdd6dc,#6f7f88 45%,#2f3a40)" role="img" aria-label="Tray of catering canapés"></div>
  <div class="abs feature-label" style="left:100px;width:310px">OFFER</div>
  <div class="photo feature" style="left:422px;width:324px;background:linear-gradient(160deg,#f2efe8,#d8cfbf 40%,#8d7a60)" role="img" aria-label="Banquet table set with plated dishes"></div>
  <div class="abs feature-label" style="left:422px;width:324px">SERVICES</div>
  <div class="photo feature" style="left:760px;width:325px;background:radial-gradient(circle at 55% 50%,#b8563e,#6e8f3a 35%,#f4f4f0 60%,#2a2a2a)" role="img" aria-label="Gourmet plated dish with fresh greens"></div>
  <div class="abs feature-label" style="left:760px;width:325px">QUALITY FOOD</div>
</section>

<section class="video-section">
  <div class="photo videos" role="img" aria-label="Soft blue-grey background of fresh produce"></div>
  <h2 class="abs videos-title">VIDEOS</h2>
  <div class="abs videos-copy">
    <p>We create our videos how to prepare delicious food every week. They will show you that we are unique, not just "another catering company" and also one dedicated to first class food and service.</p>
    <p>The cooking equipment is modern and very well maintained. This ensures the total consistency of the finished product.</p>
  </div>

  <div class="abs video-card" style="left:358px;top:1312px;width:230px;height:208px">
    <div class="video-thumb" style="height:158px;background:linear-gradient(135deg,#e9ece6,#b7c0a8 50%,#7a8670)" role="img" aria-label="Blended food in a glass">
      <svg width="34" height="34" viewBox="0 0 34 34"><circle cx="17" cy="17" r="16" fill="rgba(255,255,255,.85)"/><path d="M13 10l11 7-11 7z" fill="#444"/></svg>
    </div>
    <p class="video-cap">Blending food not only has added health benefits, but it also allows you to create unique and delicious recipes</p>
  </div>
  <div class="abs video-card" style="left:608px;top:1312px;width:230px;height:208px">
    <div class="video-thumb" style="height:160px;background:radial-gradient(circle at 50% 60%,#f6e2b8,#e6a05a 40%,#b23a2c 75%)" role="img" aria-label="Peach dessert with cream">
      <svg width="34" height="34" viewBox="0 0 34 34"><circle cx="17" cy="17" r="16" fill="rgba(255,255,255,.85)"/><path d="M13 10l11 7-11 7z" fill="#444"/></svg>
    </div>
    <p class="video-cap">Take perfectly ripe peaches, add a splash of cream, and you've got a dessert that's just right...</p>
  </div>
  <div class="abs video-card" style="left:852px;top:1312px;width:233px;height:208px">
    <div class="video-thumb" style="height:160px;background:radial-gradient(circle at 50% 50%,#e59b6f,#7fa85a 40%,#f3f3f0 65%)" role="img" aria-label="Salmon with summer vegetables">
      <svg width="34" height="34" viewBox="0 0 34 34"><circle cx="17" cy="17" r="16" fill="rgba(255,255,255,.85)"/><path d="M13 10l11 7-11 7z" fill="#444"/></svg>
    </div>
    <p class="video-cap">Fresh salmon and summer vegetables, blended with simple seasonings, make a perfect and easy dinner</p>
  </div>

  <div class="abs video-card" style="left:358px;top:1542px;width:230px;height:215px">
    <div class="video-thumb" style="height:165px;background:radial-gradient(circle at 50% 50%,#d84a3a,#7aa452 40%,#f1f0ea 70%)" role="img" aria-label="Fresh mixed salad">
      <svg width="34" height="34" viewBox="0 0 34 34"><circle cx="17" cy="17" r="16" fill="rgba(255,255,255,.85)"/><path d="M13 10l11 7-11 7z" fill="#444"/></svg>
    </div>
    <p class="video-cap">Salads can be healthy, satisfying meals on their own or perfect sides. Here is a great selection of salad!</p>
  </div>
  <div class="abs video-card" style="left:608px;top:1620px;width:230px;height:137px">
    <div class="video-thumb" style="height:100px;background:radial-gradient(circle at 50% 50%,#f0ebe0,#c7b79b 45%,#5f6870)" role="img" aria-label="Pear and ice cream dessert">
      <svg width="34" height="34" viewBox="0 0 34 34"><circle cx="17" cy="17" r="16" fill="rgba(255,255,255,.85)"/><path d="M13 10l11 7-11 7z" fill="#444"/></svg>
    </div>
    <p class="video-cap">Pear and ice cream dessert</p>
  </div>
  <div class="abs video-card" style="left:852px;top:1542px;width:233px;height:215px">
    <div class="video-thumb" style="height:165px;background:radial-gradient(circle at 50% 55%,#e6c9a4,#b98f67 35%,#eef0f1 65%)" role="img" aria-label="Crustacean seafood dish">
      <svg width="34" height="34" viewBox="0 0 34 34"><circle cx="17" cy="17" r="16" fill="rgba(255,255,255,.85)"/><path d="M13 10l11 7-11 7z" fill="#444"/></svg>
    </div>
    <p class="video-cap">Crustaceans are among the most commonly consumed seafoods. They are healthy and really delicious food.</p>
  </div>

  <div class="abs more">
    <svg width="12" height="18" viewBox="0 0 12 18"><path d="M10 2 3 9l7 7" fill="none" stroke="#fff" stroke-width="3"/></svg>
    MORE
    <svg width="12" height="18" viewBox="0 0 12 18"><path d="M2 2l7 7-7 7" fill="none" stroke="#fff" stroke-width="3"/></svg>
  </div>
</section>

<section class="order-section">
  <div class="photo order" role="img" aria-label="Dark table with a plated dessert and cutlery"></div>
  <h2 class="abs order-title">ONLINE ORDER FOOD</h2>
  <div class="abs order-copy">
    <p>This is the form through which you can order food to your home. Carefully fill in the entry fields and press "Subscribe".</p>
    <p>When the order is ready we will bring food deliverer to the address you provided.</p>
  </div>
  <div class="abs subscribe">
    <svg width="44" height="34" viewBox="0 0 52 40"><path d="M12 22a10 10 0 0 1 4-18 12 12 0 0 1 20 0 10 10 0 0 1 4 18v4H12z" fill="#fff"/><rect x="12" y="29" width="28" height="7" fill="#fff"/></svg>
    <p>SUBSCRIBE</p>
  </div>

  <div class="field" style="top:2003px">NAME<span class="field-line"></span></div>
  <div class="field" style="top:2049px">FAMILY<span class="field-line"></span></div>
  <div class="field" style="top:2095px">HOME ADDRESS<span class="field-line"></span></div>
  <div class="field" style="top:2141px">PHONE<span class="field-line"></span></div>
  <div class="field" style="top:2187px">HOUR DELIVERY<span class="field-line"></span></div>
  <div class="field" style="top:2233px">PAYMENT<span class="field-line"></span></div>
  <div class="field" style="top:2279px;height:70px">ORDER FOOD<span class="field-line" style="height:54px"></span></div>
</section>

<footer>
  <div class="abs footer"></div>
  <div class="abs foot-rule"></div>
  <div class="abs foot-div" style="left:388px"></div>
  <div class="abs foot-div" style="left:790px"></div>
  <ul class="abs foot-nav">
    <li>- Home</li><li>- Menu</li><li>- About</li><li>- Video</li><li>- Location</li>
  </ul>
  <div class="abs foot-center">
    <svg width="28" height="24" viewBox="0 0 28 24"><path d="M14 1 1 12h4v11h7v-7h4v7h7V12h4z" fill="#fff"/></svg>
    <p>Mara Lindqvist</p>
    <p>Harbor Lane 14, 3000 Vellmar</p>
  </div>
  <div class="abs foot-mail">
    <svg width="24" height="18" viewBox="0 0 24 18"><rect x="1" y="1" width="22" height="16" fill="#fff"/><path d="M1 1l11 9 11-9" fill="none" stroke="#1f2224" stroke-width="2"/></svg>
    <p style="margin-top:8px">hello@platrixcatering.com</p>
  </div>
</footer>

</body>
</html>
```